"Rise. Shift. Thrive." Empowerment Book Cover

Hello, I need a hot, trendy, and contemporary book cover designed for my first book called "Rise. Shift. Thrive. -- 360 Bold Momentum Notes to Guide Anyone to Rise, Shift, and Thrive in Their Career & Daily Dreams."
This is my first book and I am really wanting to launch my brand with it... it would be awesome to match the inside/outside branding of the book. So we can either create the book cover to match the book guts, or update the book guts to match the cover.
Lastly, I just got a professional photoshoot done last week so we can use one of those images, or we can go with a different idea/style for the cover. The body of the book is attached. All questions welcomed, happy designing!
Target Market(s)
Gen Z, Millennials and Gen X.
Industry/Entity Type
Personal Development.
Requirements
Must have
- It must stand out and be different from other typical book covers.
Nice to have
- Success, Inspiration, Motivation, Mindset, Growth.
Should not have
- Clipart, stock art, stock look and feel.

```html
<!DOCTYPE html>
<html lang="en">
<head>
<meta charset="utf-8">
<title>Rise. Shift. Thrive. — Book Cover</title>
<link rel="stylesheet" href="https://fonts.googleapis.com/css2?family=Bebas+Neue&family=Jost:wght@400;500;600;700&display=swap">
<style>
  :root {
    --page-bg: #e2e2e2;
    --cover-light: #ffffff;
    --cover-shade: #e6e6e6;
    --ink: #15152a;
    --gold: #b07a3a;
    --gold-light: #e2a95f;
    --gold-mid: #c98f4c;
    --gold-dark: #6f4a20;
  }
  * { margin: 0; padding: 0; box-sizing: border-box; }
  html, body {
    width: 1200px;
    height: 1200px;
    overflow: hidden;
    background: var(--page-bg);
  }
  .canvas {
    position: relative;
    width: 1200px;
    height: 1200px;
    display: flex;
    justify-content: center;
  }
  .cover {
    position: relative;
    width: 800px;
    height: 1200px;
    background: linear-gradient(160deg, var(--cover-shade) 0%, var(--cover-light) 45%, var(--cover-light) 55%, var(--cover-shade) 100%);
    text-align: center;
  }
  .count {
    position: absolute;
    top: 60px;
    left: 0;
    width: 100%;
    font-family: "Jost", sans-serif;
    font-weight: 700;
    font-size: 116px;
    line-height: 1;
    letter-spacing: 0.1em;
    padding-left: 0.1em;
    color: var(--gold);
  }
  .subtitle {
    position: absolute;
    top: 175px;
    left: 0;
    width: 100%;
    font-family: "Jost", sans-serif;
    font-weight: 400;
    font-size: 34px;
    line-height: 39px;
    letter-spacing: 0.14em;
    color: var(--ink);
  }
  .title {
    position: absolute;
    top: 302px;
    left: 0;
    width: 100%;
    font-family: "Bebas Neue", sans-serif;
    font-weight: 400;
    font-size: 212px;
    line-height: 171px;
    letter-spacing: 0.01em;
  }
  .title-word {
    display: block;
    background: linear-gradient(90deg, var(--gold) 0%, var(--gold-mid) 20%, var(--gold-dark) 45%, var(--gold-dark) 52%, var(--gold) 68%, var(--gold-light) 84%, var(--gold) 100%);
    -webkit-background-clip: text;
    background-clip: text;
    color: transparent;
  }
  .tagline {
    position: absolute;
    top: 922px;
    left: 0;
    width: 100%;
    font-family: "Jost", sans-serif;
    font-weight: 500;
    font-size: 34px;
    line-height: 1;
    letter-spacing: 0.12em;
    color: var(--ink);
  }
  .author {
    position: absolute;
    top: 1078px;
    left: 0;
    width: 100%;
    font-family: "Jost", sans-serif;
    font-weight: 600;
    font-size: 46px;
    line-height: 1;
    letter-spacing: 0.2em;
    padding-left: 0.2em;
    color: var(--gold);
  }
</style>
</head>
<body>
  <main class="canvas">
    <article class="cover">
      <p class="count">360</p>
      <p class="subtitle">BOLD MOMENTUM NOTES<br>TO GUIDE ANYONE TO</p>
      <h1 class="title">
        <span class="title-word">RISE</span>
        <span class="title-word">SHIFT</span>
        <span class="title-word">THRIVE</span>
      </h1>
      <p class="tagline">IN THEIR CAREER &amp; DAILY DREAMS.</p>
      <p class="author">KARIM HADDAD</p>
    </article>
  </main>
</body>
</html>
```